Stationary package for Interior and construction company
Velvet Arch Studios
Professional
Peter Hallsey
Project Manager
Warehouse K42, Dubai Logistics Park Dubai,UAE PO Box 316052
velvetarchdxb@examplemail.test
www.velvetarchdubai.example
We require two business cards with different peoples names. #1 been Peter Hallsey the second persons details are. Simon Ravenholt, Project Manager, Warehouse K42, Dubai Logistics Park, Dubai, UAE, PO Box 316052, Cell- +971 50 6185072 Ph- +971 4 3061825 Email - s.ravenholt@velvetarchstudios.example Web - www.velvetarchstudios.example Brief, Velvet Arch Studios (VAS) is a luxury fit out and renovations company based in Dubai, UAE. VAS’s clientele are high net worth individuals. The company is looking for a suite of stationary to support their everyday business needs; this should include: • Letterheads (page 1 and page2) • Business cards (Two people) • Envelopes (A4, DL) • Notepad (A4, A5) The company would like to evoke a premium brand through chic, clean and sophisticated stationary items. Colour should not be over-used unnecessarily and the typeface should be clear to read. All artwork provided should be re-writable.
Please just use the logo, add the website to the bottom footer. open to options on layout and design.

```html
<!DOCTYPE html>
<html lang="en">
<head>
<meta charset="utf-8">
<title>Velvet Arch Studios – Business Cards</title>
<link href="https://fonts.googleapis.com/css2?family=Michroma&display=swap" rel="stylesheet">
<style>
  :root {
    --stage: #dcdedf;
    --card: #ffffff;
    --card-shade: #f1f2f3;
    --brand-blue: #2b9ed6;
    --brand-grey: #5f6c77;
    --swoosh-grey: #8e979e;
    --on-blue: #ffffff;
  }
  * { margin: 0; padding: 0; box-sizing: border-box; }
  html, body { width: 1200px; height: 768px; overflow: hidden; }
  body {
    background: var(--stage);
    font-family: "Michroma", "Helvetica Neue", Arial, sans-serif;
    position: relative;
  }
  .card {
    position: absolute;
    width: 520px;
    height: 300px;
    border-radius: 14px;
    overflow: hidden;
    background: linear-gradient(160deg, var(--card) 0%, var(--card) 55%, var(--card-shade) 100%);
    box-shadow: 0 2px 6px rgba(0,0,0,0.12);
  }
  .card--back { left: 50px; top: 234px; }
  .card--front { left: 630px; top: 234px; }

  .wordmark {
    display: flex;
    align-items: center;
    gap: 12px;
    color: var(--brand-grey);
    font-size: 17px;
    letter-spacing: 0.06em;
    text-transform: uppercase;
    white-space: nowrap;
  }
  .wordmark__dot {
    width: 34px; height: 34px;
    border-radius: 50%;
    background: var(--brand-blue);
    flex: none;
  }
  .card--back .wordmark {
    position: absolute; left: 0; right: 0; top: 132px;
    justify-content: center;
  }
  .card--front .wordmark {
    position: absolute; left: 0; right: 0; top: 58px;
    justify-content: center;
  }

  .band { position: absolute; left: 0; top: 0; width: 520px; height: 300px; }

  .holder {
    position: absolute; left: 24px; top: 194px; width: 196px;
    color: var(--on-blue);
  }
  .holder__name { font-size: 10px; letter-spacing: 0.08em; }
  .holder__role { font-size: 7px; letter-spacing: 0.06em; margin-top: 5px; opacity: 0.9; }
  .holder__address { font-size: 6.5px; letter-spacing: 0.04em; margin-top: 14px; line-height: 1.7; }

  .divider {
    position: absolute; left: 226px; top: 194px;
    width: 1px; height: 88px; background: var(--on-blue); opacity: 0.8;
  }
  .contacts {
    position: absolute; left: 240px; top: 190px;
    list-style: none; color: var(--on-blue);
    font-size: 7px; letter-spacing: 0.04em;
    white-space: nowrap;
  }
  .contacts li { display: flex; align-items: center; gap: 7px; height: 15px; }
  .contacts svg { width: 9px; height: 9px; flex: none; }
</style>
</head>
<body>

  <section class="card card--back" aria-label="Business card, reverse side">
    <div class="wordmark"><span class="wordmark__dot"></span>Velvet Arch Studios</div>
  </section>

  <section class="card card--front" aria-label="Business card, front side">
    <svg class="band" viewBox="0 0 520 300" aria-hidden="true">
      <path d="M0 178 Q250 138 520 150 L520 300 L0 300 Z" fill="var(--brand-blue)"/>
      <path d="M0 168 Q250 124 520 140" fill="none" stroke="var(--swoosh-grey)" stroke-width="3"/>
    </svg>

    <div class="wordmark"><span class="wordmark__dot"></span>Velvet Arch Studios</div>

    <div class="holder">
      <p class="holder__name">Peter Hallsey</p>
      <p class="holder__role">Project Manager</p>
      <p class="holder__address">Warehouse K42,<br>Dubai Logistics Park<br>Dubai, UAE, PO Box 316052</p>
    </div>

    <div class="divider"></div>

    <ul class="contacts">
      <li><svg viewBox="0 0 10 10"><path d="M2 1 L4 1 L4.6 3 L3.4 3.8 Q4.3 5.7 6.2 6.6 L7 5.4 L9 6 L9 8 Q5 9 2.4 6.4 Q0.8 4 2 1Z" fill="var(--on-blue)"/></svg>+971 50 6185072</li>
      <li><svg viewBox="0 0 10 10"><path d="M2 1 L4 1 L4.6 3 L3.4 3.8 Q4.3 5.7 6.2 6.6 L7 5.4 L9 6 L9 8 Q5 9 2.4 6.4 Q0.8 4 2 1Z" fill="var(--on-blue)"/></svg>+971 4 3061825</li>
      <li><svg viewBox="0 0 10 10"><path d="M2 1 L4 1 L4.6 3 L3.4 3.8 Q4.3 5.7 6.2 6.6 L7 5.4 L9 6 L9 8 Q5 9 2.4 6.4 Q0.8 4 2 1Z" fill="var(--on-blue)"/></svg>+971 4 3061826</li>
      <li><svg viewBox="0 0 10 10"><rect x="0.8" y="2" width="8.4" height="6" fill="none" stroke="var(--on-blue)" stroke-width="1"/><path d="M1 2.3 L5 5.3 L9 2.3" fill="none" stroke="var(--on-blue)" stroke-width="1"/></svg>velvetarchdxb@examplemail.test</li>
      <li><svg viewBox="0 0 10 10"><circle cx="5" cy="5" r="4" fill="none" stroke="var(--on-blue)" stroke-width="1"/><path d="M1 5 H9 M5 1 Q2.5 5 5 9 M5 1 Q7.5 5 5 9" fill="none" stroke="var(--on-blue)" stroke-width="0.8"/></svg>www.velvetarchdubai.example</li>
    </ul>
  </section>

</body>
</html>
```